Business Card Design

We need a Business card design for our Family Dental Clinic.
Colour choices - White, blue and golden to go with the logo.
Industry/Entity Type
Business
Contact Information for Business Card
Side 1
DR MONA PELLINGHAM
BDS
Suite 6, Level 2, 418 Wexbridge Street
Fernvale North, Vic 3071
Fax : 9476 2035
Email: info@fernvaledentalgroup.com.au
Website: fernvaledentalgroup.com.au
Phone(image) - 9476 2035 (bigger size)
Please make sure that you produce 3 files with the same design
1) As per above
2) With out the Name ( i. e DR Mona Pellingham BDS)
3) Just the card template (no texts)
Side 2
......................................... at ........................
Please give 24 hours notice if you cannot keep this appointment

```html
<!DOCTYPE html>
<html lang="en">
<head>
<meta charset="utf-8">
<title>Fernvale Dental Group – Business Card</title>
<link href="https://fonts.googleapis.com/css2?family=Cinzel:wght@400;600&family=Crimson+Pro:wght@400;500&display=swap" rel="stylesheet">
<style>
  :root {
    --brand-blue: #1f77bc;
    --bright-blue: #1e8fd6;
    --glow-blue: #2ea3df;
    --gold: #d8a73a;
    --ink: #111111;
    --paper: #ffffff;
    --rule-blue: #5aa6dc;
  }
  * { margin: 0; padding: 0; box-sizing: border-box; }
  html, body { width: 1200px; height: 1000px; overflow: hidden; }
  body {
    position: relative;
    background: linear-gradient(to bottom, var(--brand-blue) 0 500px, var(--paper) 500px 1000px);
    font-family: "Crimson Pro", Georgia, serif;
    color: var(--ink);
  }
  .card {
    position: absolute;
    left: 263px;
    width: 673px;
    height: 415px;
  }
  .card-front { top: 30px; background: var(--paper); }
  .card-back {
    top: 555px;
    background: radial-gradient(circle at 337px 215px, var(--glow-blue) 0, var(--brand-blue) 150px);
    color: var(--paper);
  }
  .frame {
    position: absolute;
    left: 39px;
    width: 595px;
  }
  .card-front .frame { top: 46px; height: 323px; border: 1px solid var(--rule-blue); border-radius: 2px; }
  .card-back .frame { top: 46px; height: 322px; border: 1px solid rgba(255,255,255,0.75); border-radius: 2px; }

  /* front */
  .brand-mark {
    position: absolute; left: 297px; top: 62px;
    width: 80px; height: 80px; border-radius: 50%;
    background: var(--gold);
  }
  .brand-name {
    position: absolute; left: 0; right: 0; top: 168px;
    text-align: center;
    font-family: "Cinzel", Georgia, serif;
    font-weight: 600; font-size: 30px; letter-spacing: 1px;
    color: var(--bright-blue);
  }
  .practitioner {
    position: absolute; left: 0; right: 0; top: 236px;
    text-align: center;
    font-family: "Cinzel", Georgia, serif;
    font-weight: 600; font-size: 20px;
  }
  .practitioner .credential { font-weight: 400; font-size: 18px; }
  .phone-main {
    position: absolute; left: 264px; top: 280px;
    display: flex; align-items: center; gap: 8px;
    font-size: 27px; line-height: 1;
  }
  .phone-icon { width: 21px; height: 21px; }
  .address, .contacts {
    position: absolute; top: 314px;
    font-size: 12px; line-height: 14.5px;
  }
  .address { left: 64px; }
  .contacts { right: 64px; text-align: right; }
  .contacts .label { color: var(--bright-blue); }

  /* back */
  .appt-title {
    position: absolute; left: 0; right: 0; top: 52px;
    text-align: center;
    font-family: "Cinzel", Georgia, serif;
    font-size: 35px; line-height: 1; letter-spacing: 0.5px;
  }
  .col-head {
    position: absolute; top: 111px;
    font-family: "Cinzel", Georgia, serif;
    font-weight: 600; font-size: 16px; line-height: 1;
  }
  .day { width: 24px; text-align: center; }
  .slot {
    position: absolute; background: var(--paper); border-radius: 3px; height: 24px;
  }
  .slot-day { width: 24px; }
  .slot-wide { width: 153px; }
  .notice {
    position: absolute; left: 0; right: 0; top: 333px;
    text-align: center; font-size: 20px;
  }
</style>
</head>
<body>

<section class="card card-front" aria-label="Card front">
  <div class="frame"></div>
  <div class="brand-mark"></div>
  <div class="brand-name">Fernvale Dental Group</div>
  <div class="practitioner">Dr. Mona Pellingham, <span class="credential">BDS</span></div>
  <div class="phone-main">
    <svg class="phone-icon" viewBox="0 0 21 21" aria-hidden="true">
      <rect width="21" height="21" fill="var(--bright-blue)"/>
      <path d="M6 4 L9 4 L10 8 L8 9.5 C9 12 10 13 12 14 L13.5 12 L17 13 L17 16 C17 17 16 17.5 15 17.5 C9 17 4 12 3.5 6 C3.5 5 4.5 4 6 4 Z" fill="#fff"/>
    </svg>
    <span>9476 2035</span>
  </div>
  <address class="address" style="font-style:normal">
    Suite 6, Level 2,<br>
    418 Wexbridge Street,<br>
    Fernvale North, Vic 3071
  </address>
  <div class="contacts">
    <span class="label">fax:</span> 9476 2035<br>
    <span class="label">email:</span> info@fernvaledentalgroup.com.au<br>
    <span class="label">website:</span> fernvaledentalgroup.com.au
  </div>
</section>

<section class="card card-back" aria-label="Card back">
  <div class="frame"></div>
  <h1 class="appt-title" style="font-weight:400">YOUR NEXT APPOINTMENT IS</h1>

  <div class="col-head day" style="left:53px">M</div>
  <div class="col-head day" style="left:85px">T</div>
  <div class="col-head day" style="left:117px">W</div>
  <div class="col-head day" style="left:149px">T</div>
  <div class="col-head day" style="left:181px">F</div>
  <div class="col-head" style="left:260px;width:153px;text-align:center">DATE</div>
  <div class="col-head" style="left:467px;width:153px;text-align:center">TIME</div>

  <!-- row 1 -->
  <div class="slot slot-day" style="left:53px;top:132px"></div>
  <div class="slot slot-day" style="left:85px;top:132px"></div>
  <div class="slot slot-day" style="left:117px;top:132px"></div>
  <div class="slot slot-day" style="left:149px;top:132px"></div>
  <div class="slot slot-day" style="left:181px;top:132px"></div>
  <div class="slot slot-wide" style="left:260px;top:132px"></div>
  <div class="slot slot-wide" style="left:467px;top:132px"></div>
  <!-- row 2 -->
  <div class="slot slot-day" style="left:53px;top:168px"></div>
  <div class="slot slot-day" style="left:85px;top:168px"></div>
  <div class="slot slot-day" style="left:117px;top:168px"></div>
  <div class="slot slot-day" style="left:149px;top:168px"></div>
  <div class="slot slot-day" style="left:181px;top:168px"></div>
  <div class="slot slot-wide" style="left:260px;top:168px"></div>
  <div class="slot slot-wide" style="left:467px;top:168px"></div>
  <!-- row 3 -->
  <div class="slot slot-day" style="left:53px;top:204px"></div>
  <div class="slot slot-day" style="left:85px;top:204px"></div>
  <div class="slot slot-day" style="left:117px;top:204px"></div>
  <div class="slot slot-day" style="left:149px;top:204px"></div>
  <div class="slot slot-day" style="left:181px;top:204px"></div>
  <div class="slot slot-wide" style="left:260px;top:204px"></div>
  <div class="slot slot-wide" style="left:467px;top:204px"></div>
  <!-- row 4 -->
  <div class="slot slot-day" style="left:53px;top:240px"></div>
  <div class="slot slot-day" style="left:85px;top:240px"></div>
  <div class="slot slot-day" style="left:117px;top:240px"></div>
  <div class="slot slot-day" style="left:149px;top:240px"></div>
  <div class="slot slot-day" style="left:181px;top:240px"></div>
  <div class="slot slot-wide" style="left:260px;top:240px"></div>
  <div class="slot slot-wide" style="left:467px;top:240px"></div>
  <!-- row 5 -->
  <div class="slot slot-day" style="left:53px;top:276px"></div>
  <div class="slot slot-day" style="left:85px;top:276px"></div>
  <div class="slot slot-day" style="left:117px;top:276px"></div>
  <div class="slot slot-day" style="left:149px;top:276px"></div>
  <div class="slot slot-day" style="left:181px;top:276px"></div>
  <div class="slot slot-wide" style="left:260px;top:276px"></div>
  <div class="slot slot-wide" style="left:467px;top:276px"></div>

  <p class="notice">Please give 24 hours notice if you cannot keep this appointment</p>
</section>

</body>
</html>
```